Instant Broth for Ramen and Soup - Need labels for three flavors

We are a new company planning to launch a line of all natural powdered instant broth for ramen and soups. We need a logo design for our three launch flavors which will be Chicken, Prime Beef and Garden Vegetable. The powdered broth will be sold in 4oz containers with a white cap.
We would like the logo to be at the top of the label and or product description "Instant Broth for Ramen and Soups" underneath. The product description should stand out to the consumer, so it should likely be a larger font and one that compliments the logo. Below the Product description, we would like the name of the flavor and appropriate color scheme to match the flavor (see product picture for color). The design for each flavor should be the same, the only thing that should change is the color scheme to match flavor. Because we use all natural ingredients we would also like the label to state "Natural Ingredients" and "Gluten Free" on the front.
Additionally if you could please include placeholders for the nutritional label, ingredients list beneath, net size/weight on the side, bar code and a placeholder address for "Wexley Pantry LLC" that would be great as we are still finalizing these details. We would also like the label design to be catchy and interesting while complimenting the fun light-hearted logo.
Lastly, if your design is chosen you will be our main choice for additional design work (if you wish) including, top label design for the cap, finalizing the product info, formatting actual jar dimensions and other design work for the many other additional flavors we will be releasing.
Target Market(s)
Homemade ramen and soup connoisseurs, health conscious consumers, millennials and college students
Industry/Entity Type
It Company
Other font styles liked:
- SingleSleeve
Colors
Designer to choose colors to be used in the design.
Requirements
Must have
- 1) Logo
- 2) Product description "Instant Broth for Ramen and Soups"
- 3) Flavor title and color scheme
- 4) "Natural Ingredients" and "Gluten Free"
- 5) Place holder info for BQH required information (nutrition facts, net weight etc.)
Nice to have
- 1) Instructions (placeholder)
- 2) Additional info about the product (placeholder)

```html
<!DOCTYPE html>
<html lang="en">
<head>
<meta charset="utf-8">
<title>Simmerly Instant Broth – Chicken Label</title>
<link rel="stylesheet" href="https://fonts.googleapis.com/css2?family=Chewy&family=Arimo:wght@700&display=swap">
<style>
  :root {
    --band-gold: #e2b31a;
    --band-gold-dark: #c9980f;
    --leaf-green: #4a9a2e;
    --rule-gold: #e8b917;
    --muted-grey: #8a8a8a;
    --ink: #1a1a1a;
    --badge-brown: #b58a22;
    --badge-text: #fdf6e3;
    --paper: #ffffff;
    --chicken-gold: #f5b21c;
    --chicken-orange: #ee8a12;
    --bowl-green: #5aa52a;
  }
  html, body {
    margin: 0;
    padding: 0;
    width: 1200px;
    height: 994px;
    overflow: hidden;
    background: var(--paper);
  }
  .label {
    position: relative;
    width: 1200px;
    height: 994px;
    background: var(--paper);
    overflow: hidden;
    font-family: "Chewy", "Comic Sans MS", cursive;
  }
  .band {
    position: absolute;
    left: 0;
    width: 1200px;
    height: 62px;
    background: linear-gradient(var(--band-gold), var(--band-gold-dark));
  }
  .band--top { top: 0; }
  .band--bottom { bottom: 0; }
  .brand {
    position: absolute;
    top: 88px;
    left: 0;
    width: 1200px;
    text-align: center;
    font-size: 62px;
    line-height: 1;
    color: var(--ink);
    letter-spacing: 1px;
  }
  .headline {
    position: absolute;
    left: 0;
    width: 1200px;
    margin: 0;
    text-align: center;
    color: var(--leaf-green);
    font-weight: 400;
    font-size: 124px;
    line-height: 1;
  }
  .headline--top { top: 176px; }
  .headline--bottom { top: 412px; }
  .connector {
    position: absolute;
    top: 340px;
    left: 0;
    width: 1200px;
    height: 80px;
  }
  .connector__rule {
    position: absolute;
    top: 38px;
    height: 4px;
    width: 330px;
    background: var(--rule-gold);
  }
  .connector__rule--left { left: 186px; }
  .connector__rule--right { left: 666px; }
  .connector__word {
    position: absolute;
    left: 0;
    width: 1200px;
    text-align: center;
    top: 0;
    font-size: 76px;
    line-height: 1;
    color: var(--muted-grey);
  }
  .flavor-art {
    position: absolute;
    left: 340px;
    top: 548px;
    width: 700px;
    height: 382px;
    border-radius: 48% 48% 30% 30%;
    background: radial-gradient(ellipse at 48% 38%, var(--chicken-gold) 0%, var(--chicken-orange) 48%, var(--bowl-green) 70%);
  }
  .flavor-name {
    position: absolute;
    left: 440px;
    top: 690px;
    width: 440px;
    text-align: center;
    font-size: 96px;
    line-height: 1;
    color: var(--paper);
    transform: rotate(-4deg);
  }
  .claims {
    position: absolute;
    left: 90px;
    top: 600px;
    width: 290px;
    height: 176px;
  }
  .claims__shape {
    position: absolute;
    inset: 0;
  }
  .claims__text {
    position: absolute;
    left: 12px;
    top: 24px;
    width: 250px;
    text-align: center;
    font-family: "Arimo", Arial, sans-serif;
    font-weight: 700;
    font-size: 25px;
    line-height: 1.2;
    color: var(--badge-text);
  }
  .claims__text p { margin: 0; }
  .claims__text p + p { margin-top: 24px; }
</style>
</head>
<body>
  <main class="label">
    <div class="band band--top"></div>

    <div class="brand">SIMMERLY</div>

    <h1 class="headline headline--top">Instant Broth</h1>
    <div class="connector">
      <span class="connector__rule connector__rule--left"></span>
      <span class="connector__word">for</span>
      <span class="connector__rule connector__rule--right"></span>
    </div>
    <h2 class="headline headline--bottom">Ramen and Soups</h2>

    <div class="flavor-art" role="img" aria-label="Illustration of a golden roast chicken in a green bowl with scattered herb leaves and spice flecks"></div>
    <div class="flavor-name">chicken</div>

    <div class="claims">
      <svg class="claims__shape" width="290" height="176" viewBox="0 0 290 176" aria-hidden="true">
        <path fill="var(--badge-brown)" d="M138 6 C214 6 262 38 262 86 C262 104 256 118 246 130 L286 152 L232 144 C208 160 176 170 138 170 C62 170 12 134 12 88 C12 40 62 6 138 6 Z"/>
      </svg>
      <div class="claims__text">
        <p>Natural<br>Ingredients</p>
        <p>Gluten Free</p>
      </div>
    </div>

    <div class="band band--bottom"></div>
  </main>
</body>
</html>
```